Redesign This Psychology Website

We would like a slight redesign of this successful psychology (relationship counselling) website:

www.TheLumaHaven.com.au

We are updating the website, and we'd like a slight refresh of the design and style.

Please keep to very similar colours, and use the same logo. We're looking for around 10 page templates, however the main one is the home page.

Keep in mind, this website already converts quite well, so we want a new, fresh design in keeping with this one. Please don't bother designing something too extremely different.

thanks :)
Updates

Target Market(s)

couples who are looking for relationship counselling. Men and women, 25 - 70, across Australia

Industry/Entity Type

Psychology

Number of Pages Required

5+ page

Font styles to use
Sans Serif

Colors
87cfc6
b7a5cd
ec1f27
ffffff
cee9f5

Requirements
Must have
• a similar look to the current design, just looking for a slight refresh.
• Search bar
• Areas for lots of photos
• same logo
• lots of content areas
Nice to have
• great content areas, where we can display a lot of content and our areas.
Should not have
• no colors like orange, etc.
• should not have a totally different feel.

```html
<!DOCTYPE html>
<html lang="en">
<head>
<meta charset="utf-8">
<title>The Luma Haven – Relationship Counselling</title>
<link rel="stylesheet" href="https://fonts.googleapis.com/css2?family=Open+Sans:wght@400;600;700&display=swap">
<style>
:root{
  --teal:#0e7f8c;
  --teal-dark:#0a6673;
  --teal-deep:#085a66;
  --mint:#87cfc6;
  --mint-soft:#dff2ef;
  --lavender:#b7a5cd;
  --lavender-soft:#ece6f3;
  --sky:#cee9f5;
  --sky-light:#e6f4fa;
  --grey:#eef3f4;
  --white:#ffffff;
  --red:#ec1f27;
  --ink:#1e2a2d;
  --text:#1b7a87;
}
*{box-sizing:border-box;margin:0;padding:0}
html,body{width:1200px;height:3390px;overflow:hidden}
body{font-family:"Open Sans",Arial,sans-serif;color:var(--text);background:var(--white);font-size:12.5px;line-height:1.55;display:flex;flex-direction:column}
a{color:var(--teal-dark);font-weight:700;text-decoration:underline}
.wrap{width:856px;margin:0 auto;position:relative}

/* top strip */
.top-strip{height:40px;background:var(--teal-deep);flex:none}
.top-strip .wrap{height:40px;display:flex;align-items:center;justify-content:space-between}
.phone{display:flex;align-items:center;gap:8px;font-weight:700;font-size:13px;color:var(--white)}
.top-tools{display:flex;align-items:center;gap:14px}
.search{display:flex;align-items:center;width:240px;height:26px;background:var(--white);border-radius:13px;padding:0 4px 0 12px}
.search span{flex:1;font-size:11.5px;color:#8a9a9e}
.search i{width:20px;height:20px;border-radius:50%;background:var(--mint);display:flex;align-items:center;justify-content:center}
.social-top{display:flex;gap:6px}
.social-top span{width:26px;height:26px;border-radius:50%;background:var(--mint)}

/* header */
.masthead{height:118px;background:var(--grey);display:flex;align-items:center;justify-content:center;flex:none}
.brand{display:flex;align-items:center;gap:16px}
.brand-dot{width:58px;height:58px;border-radius:50%;background:var(--teal)}
.brand-name{font-size:42px;font-weight:600;color:var(--teal);line-height:1}
.brand-tag{font-size:16px;font-weight:600;color:var(--teal);margin-top:6px}

/* nav */
.main-nav{height:37px;background:var(--teal);flex:none}
.main-nav ul{list-style:none;display:flex;justify-content:space-between;align-items:center;height:37px}
.main-nav li{color:var(--white);font-weight:700;font-size:11.5px;white-space:nowrap}
.main-nav li.active{background:var(--mint);color:var(--teal-deep);padding:2px 8px;border-radius:3px}

/* hero */
.hero{height:433px;position:relative;flex:none;background:linear-gradient(100deg,var(--lavender) 0%,var(--lavender-soft) 25%,var(--sky) 50%,var(--mint) 78%,#5fb3aa 100%)}
.hero-callout{position:absolute;left:500px;top:112px;width:540px;padding:18px 24px;background:rgba(255,255,255,.8);border-left:6px solid var(--teal);border-radius:4px;font-size:36px;font-weight:600;line-height:1.4;color:var(--teal);white-space:nowrap}

/* content */
.content{padding:34px 0 22px;flex:none}
h2{font-size:21px;font-weight:700;color:var(--teal-dark);margin:0 0 9px;padding-left:12px;border-left:4px solid var(--mint);line-height:1.3}
h2.lg{font-size:22px}
.content p{margin-bottom:12px}
.section{margin-bottom:14px}
.issues{display:flex;justify-content:space-between;margin-top:4px}
.issues h3{font-size:13px;font-weight:700;color:var(--teal-dark);margin-bottom:4px}
.issue-cols,.loc-cols{display:grid;grid-template-columns:258px 200px}
.issue-cols ul,.loc-cols ul,.links{list-style:none}
.issue-cols li,.loc-cols li,.links li{display:flex;align-items:center;gap:9px;font-size:11.5px;line-height:19.5px}
.issue-cols li::before,.loc-cols li::before,.links li::before{content:"";width:10px;height:10px;border:1.5px solid var(--teal);border-radius:50%;flex:none;background:var(--mint-soft)}
.photo{background:linear-gradient(180deg,var(--lavender-soft),var(--lavender) 55%,var(--teal));border-radius:6px;box-shadow:0 4px 12px rgba(14,127,140,.18)}
.issues .photo{width:366px;height:178px}
.cards{display:flex;justify-content:space-between;margin:18px 0 30px}
.card{width:418px;height:168px;border-radius:6px;position:relative;display:flex;flex-direction:column;align-items:center;justify-content:center;gap:6px;overflow:hidden;box-shadow:0 4px 12px rgba(14,127,140,.18)}
.card-art{position:absolute;inset:0}
.card.assess .card-art{background:linear-gradient(90deg,var(--lavender-soft),var(--white) 60%,var(--lavender-soft))}
.card.about .card-art{background:linear-gradient(90deg,var(--white),var(--sky-light) 60%,var(--sky))}
.card-label{position:relative;text-align:center;font-size:21px;font-weight:700;color:var(--teal-dark);text-decoration:underline;line-height:1.3}
.card-title{position:relative;font-size:44px;color:var(--mint);font-weight:400;letter-spacing:1px;line-height:1}
.locations{display:flex;justify-content:space-between;margin-top:4px}
.video{width:366px;height:186px;margin-top:-22px;position:relative;border-radius:6px;background:linear-gradient(100deg,#2f4f57,var(--lavender) 50%,var(--teal-dark));display:flex;align-items:center;justify-content:center}
.video-title{position:absolute;left:10px;top:6px;font-size:10px;color:var(--white)}
.play{width:52px;height:36px;border-radius:9px;background:var(--red);display:flex;align-items:center;justify-content:center}
.links{margin:-4px 0 12px}
.links li{font-size:12.5px;line-height:20px}

/* quote band */
.quote-band{height:350px;flex:none;background:linear-gradient(135deg,var(--sky) 0%,var(--sky-light) 40%,var(--lavender-soft) 75%,var(--sky) 100%);padding-top:30px}
.quote{text-align:center;font-size:38px;line-height:1.22;color:var(--ink)}
.author{display:flex;align-items:center;gap:26px;margin:24px 0 0 300px}
.portrait{width:172px;height:172px;border-radius:50%;border:6px solid var(--white);background:radial-gradient(circle at 50% 40%,var(--white),var(--lavender) 65%,var(--teal))}
.author-text{font-size:13px;color:var(--ink);line-height:1.55}
.author-text strong{display:block}

/* footer */
.site-footer{flex:1;background:var(--teal);color:var(--white)}
.site-footer .wrap{display:flex;justify-content:space-between;padding-top:44px}
.foot-brand{width:220px;padding-top:50px}
.foot-brand .name{display:flex;align-items:center;gap:10px;font-size:22px;font-weight:600;white-space:nowrap}
.foot-brand .name i{width:22px;height:22px;border-radius:50%;background:var(--white);display:block}
.foot-social{display:flex;gap:22px;margin-top:50px}
.foot-social span{width:46px;height:46px;border:2px solid var(--white);border-radius:50%}
.foot-head{font-size:17px;font-weight:700;text-decoration:underline;margin-bottom:6px;line-height:1.3}
.tweets{width:268px}
.tweet-box{background:var(--teal-deep);border-radius:6px;padding:8px}
.tweet-box .tb-head{text-align:center;font-weight:700;font-size:14px;line-height:1.25;padding:6px 0 10px;border-bottom:1px solid rgba(255,255,255,.2)}
.tweet{display:flex;gap:10px;padding:9px 4px;border-bottom:1px solid rgba(255,255,255,.2);font-size:10.5px;line-height:1.4}
.tweet .av{width:26px;height:26px;border-radius:50%;background:var(--mint);flex:none}
.tweet .body{flex:1}
.tweet .meta{display:flex;justify-content:space-between;margin-top:4px;color:var(--sky)}
.heart{color:var(--red)}
.blog{width:296px}
.post{display:flex;gap:14px;margin-bottom:18px}
.post .thumb{width:126px;height:100px;flex:none;border-radius:4px;background:linear-gradient(135deg,var(--lavender-soft),var(--lavender))}
.post h4{font-size:14px;font-weight:700;line-height:1.35}
.post small{display:block;font-size:10px}
.post .btn{display:inline-block;margin-top:8px;background:var(--mint);color:var(--teal-deep);font-weight:700;border-radius:3px;padding:3px 14px;font-size:12px}

.bottom-bar{height:45px;flex:none;background:var(--teal-deep);color:var(--white);font-size:11px;font-weight:700}
.bottom-bar .wrap{height:45px;display:flex;align-items:center}
</style>
</head>
<body>

<div class="top-strip">
  <div class="wrap">
    <div class="phone">
      <svg width="12" height="18" viewBox="0 0 12 18"><rect x="1" y="1" width="10" height="16" rx="2" fill="none" stroke="#fff" stroke-width="2"/><circle cx="6" cy="14" r="1.2" fill="#fff"/></svg>
      1300 555 018
    </div>
    <div class="top-tools">
      <div class="search"><span>Search the site…</span><i><svg width="10" height="10" viewBox="0 0 10 10"><circle cx="4" cy="4" r="3" fill="none" stroke="#085a66" stroke-width="1.6"/><path d="M6.3 6.3 L9 9" stroke="#085a66" stroke-width="1.6"/></svg></i></div>
      <div class="social-top" aria-label="Social links"><span></span><span></span><span></span></div>
    </div>
  </div>
</div>

<header class="masthead">
  <div class="brand">
    <div class="brand-dot"></div>
    <div>
      <div class="brand-name">The Luma Haven</div>
      <div class="brand-tag">helping you create loving relationships</div>
    </div>
  </div>
</header>

<nav class="main-nav">
  <ul class="wrap">
    <li class="active">Home</li><li>About us</li><li>Resources</li><li>Blogs</li><li>Counselling types</li><li>Relationship Counselling Locations</li><li>Sex Therapy locations</li><li>Quizzes</li><li>F.A.Q.'S</li><li>Contact us</li>
  </ul>
</nav>

<section class="hero" role="img" aria-label="Smiling couple embracing outdoors in soft sunlight">
  <div class="hero-callout">We can help you find<br>the love that seems<br>lost under the problems</div>
</section>

<main class="content">
  <div class="wrap">
    <section class="section">
      <h2>We Specialise in Relationship &amp; Marriage Counselling :</h2>
      <p>At The Luma Haven, we are a group of <strong style="font-size:14px">PSYCHOLOGISTS</strong>, Australia wide who are <a>passionate about relationships and helping you with yours.</a></p>
      <p>Our vision is to provide the most highly regarded and comprehensive <a>marriage counselling</a> and <a>relationship counselling</a>, and <a>sex therapy</a> in Australia, at reasonable and affordable rates.'</p>
      <p>When we are experiencing relationship and marriage problems, there can be a lot of pain and confusion, and it can often be difficult to cope with the other areas of our lives when we are struggling with problems with our partner.</p>
      <p>We are not taught about relationships and how to have a good one in our schools, so most of us are doing the best we know how, but lack the knowledge on how to create a better relationship.</p>
    </section>

    <section class="section">
      <h2 class="lg">Our Luma Haven Psychologists :</h2>
      <p>Our team of 75 hand chosen <strong>Registered Psychologists</strong> in 81 locations Australia wide, are individually selected for their knowledge, experience, compassion, and unbiased approach to marriage counselling and sexual therapy.</p>
      <p>In addition all our Psychologists take part in our initial Relationship Counselling Methodologies Training and yearly in-house conferences, ensuring you are in safe and experienced hands.</p>
      <p>As we are Psychologists, you may be eligible for Medicare &amp; Private Health Insurance Rebates.We are highly experienced and can help you with all kinds of relationship difficulties.</p>
      <div class="issues">
        <div>
          <h3>Here are some of the common ones:</h3>
          <div class="issue-cols">
            <ul><li>Affairs</li><li>Verbal abuse</li><li>Lack of intimacy</li><li>Loss of love</li><li>Sexual problems</li><li>Problems with parenting your children</li><li>All forms of family problems</li><li>Porn addiction problems</li><li>Narcissism problems</li></ul>
            <ul><li>Controlling behaviour</li><li>Imbalance of power</li><li>Poor communication</li><li>Relationship neglect</li><li>Problems from childhood</li><li>Step children and in-laws</li><li>Anger management problems</li><li>Pre-marriage programs</li></ul>
          </div>
        </div>
        <div class="photo" role="img" aria-label="Couple forming a heart shape with their arms on a beach at sunset"></div>
      </div>
    </section>

    <section class="section">
      <h2 class="lg">Our Relationship Counselling Approach</h2>
      <p style="margin-bottom:2px">It is an important part of our policy to take a very positive approach to our relationship counselling.</p>
      <p>We feel it is important to really understand the problems and perspectives of each of you, and at the same time, we find that most couples are looking to find a positive action plan and way through their problems to make changes which have a positive impact and a real sense of hope for their relationship.</p>
      <p>Read more about our approach to counselling in our <a>relationship counselling sessions</a>, and <a>frequently asked questions about the relationship and marriage counselling process</a>.</p>
      <div class="cards">
        <div class="card assess">
          <div class="card-art" role="img" aria-label="Couple in a tug of war over a red heart"></div>
          <div class="card-label">Take Our<br>Luma Relationship Assessment</div>
        </div>
        <div class="card about">
          <div class="card-art" role="img" aria-label="Hand writing on a whiteboard"></div>
          <div class="card-title">ABOUT US</div>
          <div class="card-label">Find Out More About Us</div>
        </div>
      </div>
    </section>

    <section class="section">
      <h2 class="lg">Our Relationship Counselling Locations across Australia</h2>
      <p style="margin-bottom:6px">We currently have relationship counselling and marriage counselling services in:</p>
      <div class="locations">
        <div class="loc-cols">
          <ul><li><a>Sydney – 19 centres</a></li><li><a>Canberra – 2 centres</a></li><li><a>Melbourne – 21 centres</a></li><li><a>Perth – 11 centres</a></li><li><a>Brisbane – 14 centres</a></li><li><a>Wollongong – 1 centre</a></li><li><a>Central Coast – 2 centres</a></li></ul>
          <ul><li><a>Adelaide – 4 centres</a></li><li><a>Gold Coast – 5 centres</a></li><li><a>Sunshine Coast – 2 centres</a></li><li><a>Cairns – 1 centre</a></li><li><a>Townsville – 1 centre</a></li><li><a>Wodonga – 1 centre</a></li></ul>
        </div>
        <div class="video" role="img" aria-label="Video still of a counselling session">
          <span class="video-title">What to Expect from Relationship Counselling</span>
          <div class="play"><svg width="16" height="18" viewBox="0 0 16 18"><path d="M0 0 L16 9 L0 18Z" fill="#fff"/></svg></div>
        </div>
      </div>
    </section>

    <section class="section" style="margin-top:28px">
      <h2 class="lg">Communication is a vital skill but not often taught to us.</h2>
      <p>Most people find that their ways of communicating with each other are what hamper us from having a happy healthy relationship.</p>
      <p>Effective Interpersonal Communication skills are not something that we are usually taught. But for almost everyone who is having difficulties in their relationship, they feel that they are <strong>trying to communicate their thoughts and feelings but that their partner is not listening.</strong></p>
      <p>Most people then find that they, themselves don't want to listen when they experience their partner as not wanting to listen to them, so the net effect is that neither person gets listened to, and both are frustrated.</p>
      <p>So learning how to communicate your honest thoughts and feelings in a way that your partner does truly listen is a crucial skill for you to feel that you are in a fulfilling relationship. We can show you some simple but effective principles on how to do this with each other.</p>
    </section>

    <section class="section" style="margin-bottom:0">
      <h2 class="lg">We as individuals have specific patterns in our relationships.</h2>
      <p>We can also assist you if you want <strong>individual help and guidance on your relationship</strong>, so you can learn what the patterns in your relationships are showing you about yourself.</p>
      <p>If you have been in a number of relationships and have found yourself repeating the same kind of experiences, which is often the way our relationships play out, we can help you discover the patterns that you might be unwittingly setting up, so you can change these and move into more rewarding relationships in the future.</p>
      <p>Want more information? Please help yourself to our free articles on common relationship problems you may be encountering including:</p>
      <ul class="links"><li><a>Why relationships go wrong</a></li><li><a>How to recover from an affair</a></li><li><a>Have you lost yourself in your relationship</a></li><li><a>The secret to more sex</a></li></ul>
      <p style="margin-bottom:0">For the <a>latest short, up- to- date articles on relationships</a>, relationship problems and relationship counselling, please also check out our relationship counselling <a>blog</a>.</p>
    </section>
  </div>
</main>

<section class="quote-band">
  <p class="quote">“ At the end of our life, what matters<br>most is how well did we love"</p>
  <div class="author">
    <div class="portrait" role="img" aria-label="Portrait of the centre director"></div>
    <div class="author-text">
      <p>You can read more about <a>relationship counselling</a> here.Warmly,</p>
      <p style="margin-top:12px"><strong>Maren Holt</strong><strong>Director – Psychologist</strong>Grad Dip Psych, Post Grad Dip Psych, B Ed, Dip Teach, MAPS</p>
    </div>
  </div>
</section>

<footer class="site-footer">
  <div class="wrap">
    <div class="foot-brand">
      <div class="name"><i></i>The Luma Haven</div>
      <div class="foot-social" aria-label="Social links"><span></span><span></span><span></span></div>
    </div>
    <div class="tweets">
      <div class="foot-head">LATEST TWEETS</div>
      <div class="tweet-box">
        <div class="tb-head">Tweets about<br>The Luma Haven</div>
        <div class="tweet"><div class="av"></div><div class="body">@mirafields Summer is almost here, time to slow down together<div class="meta"><span class="heart">♥</span><span>20 Mar</span></div></div></div>
        <div class="tweet"><div class="av"></div><div class="body">@mirafields Summer is almost here, time to slow down together<div class="meta"><span class="heart">♥</span><span>20 Mar</span></div></div></div>
        <div class="tweet" style="border-bottom:0"><div class="av"></div><div class="body">@mirafields Summer is almost here, time to slow down together<div class="meta"><span class="heart">♥</span><span>20 Mar</span></div></div></div>
      </div>
    </div>
    <div class="blog">
      <div class="foot-head">OUR SELECTION OF BLOG<br>POSTS ON</div>
      <div class="post">
        <div class="thumb" role="img" aria-label="Upset woman beside her partner"></div>
        <div><h4>What can I do if I'm living with a Narcissist?</h4><small>April 28, 2017</small><span class="btn">Read More</span></div>
      </div>
      <div class="post">
        <div class="thumb" role="img" aria-label="Woman turning away from a man"></div>
        <div><h4>Why am I with a Narcissist?</h4><small>February 28, 2017</small><span class="btn">Read More</span></div>
      </div>
    </div>
  </div>
</footer>

<div class="bottom-bar"><div class="wrap">2017 © COPYRIGHTS The Luma Haven</div></div>

</body>
</html>
```